Billboard advertisement design

Health & Fitness centre requires a billboard advertisement design for an allocated space out the front of the shopping centre in which it is located. Bolt Ridge Health & Fitness is located in a small town with one other competitor. Looking for a fun, trendy sign to draw people's attention and make sure Bolt Ridge is instantly recognisable. Sign location is in the middle of town on the national highway. Approximate size is 12' x 5'. Final design will encourage people who have been thinking about joining the gym to take the first step in leading a fitter and healthier lifestyle.

Target Market(s)

Health conscious members of the community that have been thinking about taking the next step and joining a gym

Industry/Entity Type

Shopping

Requirements
Must have
• Please utilise attached logo
Nice to have
• Contact info is (07) 4913 5862 info@boltridgefitness-example.com.au

```html
<!DOCTYPE html>
<html lang="en">
<head>
<meta charset="utf-8">
<title>Bolt Ridge Health &amp; Fitness – Billboard</title>
<link rel="stylesheet" href="https://fonts.googleapis.com/css2?family=Roboto+Condensed:wght@300;400;700&family=Arimo:wght@400;700&display=swap">
<style>
  :root {
    --bg-dark: #0d0d0d;
    --bg-mid: #2b2b2b;
    --photo-deep: #1a0d06;
    --photo-warm: #6b3a1c;
    --photo-glow: #a8642f;
    --label-box: #2f2f2f;
    --label-text: #d6d6d6;
    --list-text: #e6e6e6;
    --brand: #1f7fd6;
    --contact: #ffffff;
    --badge-red: #e3180f;
    --white: #ffffff;
  }
  * { margin: 0; padding: 0; box-sizing: border-box; }
  html, body { width: 1200px; height: 500px; overflow: hidden; background: var(--bg-dark); }
  .billboard {
    position: relative;
    width: 1200px;
    height: 500px;
    overflow: hidden;
    background: radial-gradient(ellipse 70% 90% at 55% 45%, var(--bg-mid) 0%, #1a1a1a 45%, var(--bg-dark) 100%);
    font-family: "Roboto Condensed", "Arial Narrow", sans-serif;
  }
  .athlete-photo {
    position: absolute;
    left: 0; top: 0;
    width: 345px; height: 500px;
    background:
      radial-gradient(ellipse 60% 45% at 45% 38%, var(--photo-glow) 0%, var(--photo-warm) 45%, transparent 80%),
      linear-gradient(90deg, var(--photo-deep) 0%, var(--photo-warm) 55%, #2a150a 85%, transparent 100%);
  }
  .focus-label {
    position: absolute;
    left: 372px; top: 116px;
    width: 89px; height: 259px;
    background: var(--label-box);
    display: flex; align-items: center; justify-content: center;
  }
  .focus-label span {
    transform: rotate(-90deg);
    font-weight: 300;
    font-size: 78px;
    color: var(--label-text);
    letter-spacing: 2px;
    white-space: nowrap;
  }
  .benefit-list {
    position: absolute;
    left: 474px; top: 124px;
    list-style: none;
  }
  .benefit-list li {
    font-size: 37px;
    line-height: 45px;
    color: var(--list-text);
    font-weight: 400;
  }
  .brand-name {
    position: absolute;
    left: 632px; top: 66px;
    width: 528px;
    text-align: center;
    color: var(--brand);
    font-weight: 700;
    font-size: 58px;
    line-height: 66px;
    white-space: nowrap;
  }
  .contact {
    position: absolute;
    left: 785px; top: 160px;
    color: var(--contact);
    font-family: "Arimo", Arial, sans-serif;
  }
  .contact .phone { font-size: 33px; line-height: 40px; }
  .contact .email { font-size: 21px; line-height: 28px; }
  .guarantee-badge {
    position: absolute;
    left: 772px; top: 274px;
    width: 246px; height: 143px;
  }
  .join-cta {
    position: absolute;
    left: 714px; top: 420px;
    width: 400px;
    text-align: center;
    font-family: "Arimo", Arial, sans-serif;
    font-size: 42px;
    color: var(--white);
    line-height: 50px;
  }
</style>
</head>
<body>
<div class="billboard">
  <div class="athlete-photo" role="img" aria-label="Photograph of a muscular athlete's shoulder and arm, glistening with sweat, lit warmly against a dark background"></div>

  <div class="focus-label"><span>BODY</span></div>
  <ul class="benefit-list">
    <li>GYM</li>
    <li>ATHLETIC</li>
    <li>MUSCLES</li>
    <li>ACTIVITY</li>
    <li>FITNESS</li>
  </ul>

  <p class="brand-name">BOLT RIDGE FITNESS</p>

  <div class="contact">
    <p class="phone">(07) 4913 5862</p>
    <p class="email">info@boltridgefitness-example.com.au</p>
  </div>

  <svg class="guarantee-badge" viewBox="0 0 246 143" aria-label="100% Quality Guarantee">
    <defs>
      <clipPath id="badge-cut"><rect x="0" y="0" width="246" height="143"/></clipPath>
    </defs>
    <circle cx="123" cy="123" r="123" fill="var(--badge-red)" clip-path="url(#badge-cut)"/>
    <text x="123" y="64" text-anchor="middle" fill="var(--white)" font-family="Arimo, Arial, sans-serif" font-weight="700" font-size="48">100%</text>
    <text x="123" y="96" text-anchor="middle" fill="var(--white)" font-family="Arimo, Arial, sans-serif" font-weight="700" font-size="30">Quality</text>
    <text x="123" y="130" text-anchor="middle" fill="var(--white)" font-family="Arimo, Arial, sans-serif" font-size="34">Guarantee</text>
  </svg>

  <p class="join-cta">JOIN NOW..!!</p>
</div>
</body>
</html>
```